R.T.Pell Logging Web design

Our website needs a redesign. We want it to appear professional and easy to navigate. We will be adding videos and pictures to the new website. We do not sell any products on our website. It should be designed for informational purposes. Our company performs timber harvesting and forest management services. Attached is our new company logo.

www.rtpelllogging-example.com if you want to see our current website.

Industry/Entity Type

Graphic Design

Coding

Coded - Design and coding required

```html
<!DOCTYPE html>
<html lang="en">
<head>
<meta charset="utf-8">
<title>R.T.Pell Logging</title>
<link href="https://fonts.googleapis.com/css2?family=PT+Sans:wght@400;700&display=swap" rel="stylesheet">
<style>
:root{
  --bar:#2b1a0e;
  --bar-deep:#1c1009;
  --accent:#e07a1f;
  --tan-1:#d9b27a;
  --tan-2:#c99a5c;
  --wood-1:#5a3014;
  --wood-2:#3e1f0b;
  --ink:#4a2a12;
  --ink-soft:#6b4a2c;
  --cream:#f5e6cf;
  --white:#ffffff;
}
*{box-sizing:border-box;margin:0;padding:0}
html,body{width:1200px;height:2472px;overflow:hidden}
body{font-family:"PT Sans",Arial,sans-serif;color:var(--ink);background:var(--bar)}
.page{position:relative;width:1200px;height:2472px}

.hero{position:absolute;top:0;left:0;width:1200px;height:520px}
.hero-photo{position:absolute;inset:0;background:linear-gradient(180deg,#6f8a3a 0%,#4d6a28 35%,#2f4a1a 70%,#4a5a24 100%)}
.topbar{position:absolute;top:0;left:0;width:1200px;height:72px;background:rgba(35,20,8,.88);border-bottom:2px solid rgba(224,122,31,.5)}
.phone{position:absolute;top:6px;left:190px;color:var(--cream);font-size:14px;display:flex;align-items:center;gap:6px}
.brand{position:absolute;top:20px;left:120px;display:flex;align-items:center;gap:8px;color:var(--cream)}
.brand-mark{width:34px;height:34px;border-radius:50%;background:var(--accent)}
.brand-name{font-size:26px;font-weight:700;letter-spacing:1px}
.nav{position:absolute;top:26px;left:624px;display:flex;gap:4px}
.nav a{color:var(--cream);text-decoration:none;font-size:14px;padding:6px 10px}
.nav a.active{background:var(--accent);color:var(--white)}
.hero-note{position:absolute;top:148px;left:176px;width:310px;color:var(--white);font-size:15px;line-height:1.35;text-shadow:0 1px 2px rgba(0,0,0,.6)}

.wood-light{background:linear-gradient(180deg,var(--tan-1),var(--tan-2))}
.wood-dark{background:linear-gradient(180deg,var(--wood-1),var(--wood-2))}

.services{position:absolute;top:520px;left:0;width:1200px;height:370px;text-align:center}
.services h2{margin-top:52px;font-weight:400;font-size:24px;color:var(--ink-soft)}
.services h2 strong{display:block;font-size:26px;color:var(--ink)}
.cards{display:flex;gap:20px;justify-content:center;margin-top:26px}
.card{width:200px;text-align:center}
.card .ph{height:112px;border:3px solid var(--cream)}
.card h3{font-size:15px;margin:10px 0 4px;color:var(--ink)}
.card p{font-size:11px;line-height:1.35;color:var(--ink-soft)}

.about{position:absolute;top:890px;left:0;width:1200px;height:382px;text-align:center;color:var(--cream)}
.about h2{margin-top:56px;font-size:26px;font-weight:400}
.about h2 strong{font-weight:700}
.about p{width:740px;margin:34px auto 0;font-size:13px;line-height:1.5;text-align:left}
.btn{display:inline-block;margin-top:58px;background:var(--accent);color:var(--white);font-size:15px;padding:8px 18px;text-decoration:none}

.gallery{position:absolute;top:1272px;left:0;width:1200px;height:560px;text-align:center}
.gallery h2,.clients-title{font-size:34px;font-weight:400;color:var(--ink)}
.gallery h2{margin-top:28px}
.rule{width:180px;height:2px;background:var(--ink-soft);margin:8px auto 0;opacity:.5}
.tabs{display:flex;gap:6px;justify-content:center;margin-top:22px}
.tabs span{font-size:11px;padding:4px 8px;background:rgba(255,255,255,.35);color:var(--ink)}
.tabs span.active{background:var(--wood-1);color:var(--cream)}
.grid{display:grid;grid-template-columns:repeat(4,200px);gap:20px;justify-content:center;margin-top:18px}
.grid .ph{height:168px;border:3px solid var(--cream)}

.clients{position:absolute;top:1832px;left:0;width:1200px;height:410px;text-align:center}
.clients-title{padding-top:20px}
.client-band{position:absolute;top:88px;left:0;width:1200px;height:322px;background:linear-gradient(180deg,#4a2610,#2e170a)}
.client-grid{display:grid;grid-template-columns:repeat(4,200px);grid-template-rows:repeat(2,150px);justify-content:center;margin-top:10px}
.client{display:flex;align-items:center;justify-content:center;gap:8px;color:var(--tan-1);font-size:17px;font-weight:700;border-right:1px solid rgba(217,178,122,.25);border-bottom:1px solid rgba(217,178,122,.25)}
.client:nth-child(4n){border-right:none}
.client:nth-child(n+5){border-bottom:none}
.client i{width:18px;height:18px;background:var(--tan-1);display:block}

.footer{position:absolute;top:2242px;left:0;width:1200px;height:178px;background:var(--bar);color:var(--cream);font-size:11px}
.f-col{position:absolute;top:22px}
.f-brand{left:160px;width:220px}
.f-brand .brand-name{font-size:22px}
.f-brand p{margin-top:10px;line-height:1.4;opacity:.8}
.f-contact{left:500px;width:220px}
.f-quick{left:776px;width:220px}
.f-col h4{font-size:12px;margin-bottom:12px;letter-spacing:.5px}
.f-contact li{list-style:none;margin-bottom:8px;display:flex;gap:6px;align-items:center;opacity:.85}
.field{height:18px;background:var(--cream);margin-bottom:6px;width:150px;border-radius:2px}
.field.tall{height:36px}
.send{display:inline-block;background:var(--accent);color:var(--white);padding:3px 10px;font-size:10px}
.bottom{position:absolute;top:2420px;left:0;width:1200px;height:52px;background:var(--bar-deep);color:var(--cream);font-size:11px;opacity:.9}
.bottom .copy{position:absolute;left:170px;top:20px}
.bottom .links{position:absolute;right:170px;top:20px}
</style>
</head>
<body>
<div class="page">

  <header class="hero">
    <div class="hero-photo" role="img" aria-label="Sunlit pine forest with tall straight trunks"></div>
    <div class="topbar">
      <div class="phone">
        <svg width="12" height="12" viewBox="0 0 24 24"><path fill="#f5e6cf" d="M6.6 10.8a15 15 0 0 0 6.6 6.6l2.2-2.2a1 1 0 0 1 1-.25 11 11 0 0 0 3.6.6 1 1 0 0 1 1 1V20a1 1 0 0 1-1 1A17 17 0 0 1 3 4a1 1 0 0 1 1-1h3.5a1 1 0 0 1 1 1 11 11 0 0 0 .6 3.6 1 1 0 0 1-.25 1z"/></svg>
        (555) 014-2280
      </div>
      <div class="brand"><span class="brand-mark"></span><span class="brand-name">R.T.PELL</span></div>
      <nav class="nav">
        <a class="active" href="#">Home</a><a href="#">About Us</a><a href="#">Services</a><a href="#">Location</a><a href="#">Contact Us</a>
      </nav>
    </div>
    <p class="hero-note">We are always buying timber in East Texas. Call for a free estimate. If you have a timber exemption on your property, call us. We can add timber management plans for free.</p>
  </header>

  <section class="services wood-light">
    <h2>R. T. Pell Logging Company provides <strong>timber harvesting and forest management services</strong></h2>
    <div class="cards">
      <div class="card"><div class="ph" role="img" aria-label="Select cut stand of pines" style="background:linear-gradient(#7d8c4a,#4d5a2a)"></div><h3>Select Cut</h3><p>Careful removal of chosen trees keeps the stand healthy and growing for future harvests.</p></div>
      <div class="card"><div class="ph" role="img" aria-label="Plantation thinning rows" style="background:linear-gradient(#8a9a5a,#55652f)"></div><h3>Plantation Thinning</h3><p>Thinning rows in planted pine gives the remaining trees room and light to grow.</p></div>
      <div class="card"><div class="ph" role="img" aria-label="Clear cut tract" style="background:linear-gradient(#9fb0c0,#8a7150)"></div><h3>Clear Cut</h3><p>Full harvest of a tract, leaving the land ready for site preparation and replanting.</p></div>
      <div class="card"><div class="ph" role="img" aria-label="Mechanical felling machine" style="background:linear-gradient(#8fa05a,#6b4a2a)"></div><h3>Mechanical Felling</h3><p>Modern felling equipment works safely and cleanly across every kind of terrain.</p></div>
    </div>
  </section>

  <section class="about wood-dark">
    <h2>About <strong>R. T. Pell Logging Company</strong></h2>
    <p>My name is R. T. Pell and I started this company in 1998. I was born and raised in the piney woods of East Texas. Growing up, I spent most of my free time in the woods helping with the family timber work. After years working for other crews, I decided to run my own business and build a team I trust. Today we harvest timber and manage forest land for landowners across the region. We treat every tract as if it were our own, protecting roads, streams and young trees. Our crews are trained, insured and proud of the work they do. Call us for a free estimate and an honest price for your timber.</p>
    <a class="btn" href="#">Read more</a>
  </section>

  <section class="gallery wood-light">
    <h2>Our Gallery</h2>
    <div class="rule"></div>
    <div class="tabs"><span class="active">View All</span><span>Select Cut</span><span>Plantation Thinning</span><span>Clear Cut</span><span>Mechanical Felling / Harvesting Services</span></div>
    <div class="grid">
      <div class="ph" role="img" aria-label="Log loader stacking timber" style="background:linear-gradient(#a4b4c4,#6a5a3e)"></div>
      <div class="ph" role="img" aria-label="Red skidder in the woods" style="background:linear-gradient(#6f8a3a,#8a3a2a)"></div>
      <div class="ph" role="img" aria-label="Harvester machine at work" style="background:linear-gradient(#7f8f5a,#3a3a2a)"></div>
      <div class="ph" role="img" aria-label="Cleared land with logs" style="background:linear-gradient(#b0c0d0,#8a7a4a)"></div>
      <div class="ph" role="img" aria-label="Crew working at a landing" style="background:linear-gradient(#6f8a3a,#4a6a2a)"></div>
      <div class="ph" role="img" aria-label="Log truck loaded with timber" style="background:linear-gradient(#c0c8d0,#7a5a3a)"></div>
      <div class="ph" role="img" aria-label="Red log trucks parked" style="background:linear-gradient(#9aaa6a,#9a2a1a)"></div>
      <div class="ph" role="img" aria-label="Feller buncher in pines" style="background:linear-gradient(#8a9a5a,#5a4a2a)"></div>
    </div>
  </section>

  <section class="clients wood-light">
    <h2 class="clients-title">Our Clients</h2>
    <div class="rule"></div>
    <div class="client-band">
      <div class="client-grid">
        <div class="client"><i></i>Ashby Timber</div>
        <div class="client"><i></i>Greenrow Forest</div>
        <div class="client"><i></i>Lindell Lumber</div>
        <div class="client"><i></i>Tomkins Mills</div>
        <div class="client"><i></i>Fenwick Fiber</div>
        <div class="client"><i></i>Delmar Wood</div>
        <div class="client"><i></i>Harlan Pulp</div>
        <div class="client"><i></i>Certa Forest</div>
      </div>
    </div>
  </section>

  <footer class="footer">
    <div class="f-col f-brand">
      <div class="brand" style="position:static"><span class="brand-mark" style="width:26px;height:26px"></span><span class="brand-name">R.T.PELL</span></div>
      <p>We are always buying timber in East Texas. Call for a free estimate. If you have a timber exemption on your property, call us. We can add timber management plans for free.</p>
    </div>
    <div class="f-col f-contact">
      <h4>CONTACT INFO</h4>
      <ul>
        <li><svg width="10" height="10" viewBox="0 0 24 24"><path fill="#e07a1f" d="M12 2a7 7 0 0 0-7 7c0 5 7 13 7 13s7-8 7-13a7 7 0 0 0-7-7zm0 9.5A2.5 2.5 0 1 1 12 6.5a2.5 2.5 0 0 1 0 5z"/></svg>PO Box 410, Cedar Bend, Texas 75010</li>
        <li><svg width="10" height="10" viewBox="0 0 24 24"><path fill="#e07a1f" d="M6.6 10.8a15 15 0 0 0 6.6 6.6l2.2-2.2a1 1 0 0 1 1-.25 11 11 0 0 0 3.6.6 1 1 0 0 1 1 1V20a1 1 0 0 1-1 1A17 17 0 0 1 3 4a1 1 0 0 1 1-1h3.5a1 1 0 0 1 1 1 11 11 0 0 0 .6 3.6 1 1 0 0 1-.25 1z"/></svg>(555) 014-2280</li>
        <li><svg width="10" height="10" viewBox="0 0 24 24"><path fill="#e07a1f" d="M3 5h18v14H3zm2 2v.5l7 4.5 7-4.5V7z"/></svg>office@rtpell-example.com</li>
      </ul>
    </div>
    <div class="f-col f-quick">
      <h4>QUICK CONTACT</h4>
      <div class="field"></div><div class="field"></div><div class="field"></div><div class="field tall"></div>
      <span class="send">Submit</span>
    </div>
  </footer>
  <div class="bottom">
    <span class="copy">© copyright information here</span>
    <span class="links">Home | About Us | Contact Us | Location | Services</span>
  </div>

</div>
</body>
</html>
```